TVF web design

We need a homepage web design concept for a new company based in Brisbane called 'Tarvel Fabrication'. They design, manufacture and repair of all forms of operator Roll Over Protective Structures or ROPS, and Falling Object Protective Structures or FOPS canopies and cabins.
Updates
Sorry link to website is incorrect should be http://www.norbeckfab.com.au/
Thanks
Hi Everyone
I am presenting designs to my client on Wednesday so will let you feedback.
Cheers
Mags
Target Market(s)
Adults in construction industry and their Agents/Distributors
Industry/Entity Type
Construction
Number of Pages Required
1 page
Requirements
Must have
- Main Navigation
- o Home
- o About Us
- - Mission and Values
- - Facilities
- - Terms and Conditions
- - Jobs
- o Rops/Fops
- o Cabins
- o Crane Repairs
- o Other Products
- o Links
- o Contact Us
- - Client wants a sleek, corporate look and feel an example of a site they like is www.corvinlode.com.au
- - Client is rebranding and I have attached some sample new brochures that contains their new corporate colours etc as a guideline for the direction they are going.
- - The following elements are to be included in the design concept:
- o Homepage
- - Room for a Flash banner of rotating images in banner
- - Phone number should appear on every page 07 4819 6307
- - Horizontal navigation (can you show how drop down will appear as well)
- - Logo is attached (bear in mind this will be changing to new corporate colours) so just use the one attached but colours need to be in line with their new colours.
- - Tagline is “It’s the choice you make, not the change you take that determines your safety!” this needs to be displayed on every page of the site.
- - New Corporate colours are orange: RGB - 239 - 179 - 47 (colour 1) to RGB 239 - 121 - 47 (colour 2) and grey: RGB - 46 - 54 – 64
- - Intro text on page somewhere
- - 3 containers/icons to highlight areas on site – Rops/Fops, Sign up to our enewsletter and Contact Us
- - Images – have attached a few that can be used in concepts.

```html
<!DOCTYPE html>
<html lang="en">
<head>
<meta charset="utf-8">
<title>Tarvel Fabrication – Web Design Concept</title>
<link href="https://fonts.googleapis.com/css2?family=Exo+2:ital,wght@0,600;0,800;1,300;1,600;1,800;1,900&family=Arimo:wght@400;700&display=swap" rel="stylesheet">
<style>
:root{
  --orange:#ef792f;
  --orange-light:#efb32f;
  --orange-mid:#f39a3c;
  --grey:#2e3640;
  --ink:#161616;
  --panel-line:#6e6e6e;
  --white:#ffffff;
  --caption:#e8e8e8;
}
*{box-sizing:border-box;margin:0;padding:0}
html,body{width:1200px;height:3037px;overflow:hidden;background:#fff}
.sheet{position:absolute;left:0;top:0;width:1024px;height:2592px;transform:scale(1.171875);transform-origin:0 0;font-family:'Arimo',Arial,sans-serif}

.sheet-label{position:absolute;left:83px;font:italic 600 21px/1 'Exo 2',sans-serif;color:var(--orange);letter-spacing:.3px}

/* mockup frame */
.mock{position:absolute;left:58px;width:902px;overflow:hidden;
  background:
    linear-gradient(90deg,rgba(0,0,0,.55),rgba(0,0,0,0) 22%,rgba(0,0,0,0) 78%,rgba(0,0,0,.55)),
    linear-gradient(180deg,#1e1e1e 0,#4d4b49 60px,#a29e99 160px,#bcb7b2 230px,#7b7875 330px,#2a2a2a 470px,#060606 600px,#000 100%);}

/* banner */
.banner{position:absolute;left:90px;top:0;width:730px;height:149px;background:linear-gradient(180deg,var(--orange-mid),var(--orange));border-radius:0 0 8px 8px}
.banner-photo{position:absolute;top:7px;height:125px}
.banner-photo span{position:absolute;right:8px;bottom:3px;font:italic 800 10.5px/1 'Exo 2',sans-serif;color:var(--white);letter-spacing:.3px}
.photo-truck{left:7px;width:235px;background:linear-gradient(135deg,#f2b21f,#d89010 55%,#3a3a36)}
.photo-fabrication{left:245px;width:232px;background:linear-gradient(135deg,#4a4a4a,#9b9b9b 50%,#565656)}
.photo-repairs{left:480px;width:232px;background:linear-gradient(135deg,#5a5a5a,#d8d8d6 55%,#b4b2ae)}

/* logo + tagline */
.brand-bar{position:absolute;left:70px;top:137px;width:372px;height:46px;background:linear-gradient(180deg,var(--orange-mid),var(--orange));border-radius:6px;padding:6px 8px}
.brand-plate{height:100%;background:linear-gradient(180deg,#2b2b2b,#0c0c0c);border-radius:3px;display:flex;align-items:center;justify-content:center;gap:10px}
.brand-name{font:600 21px/1 'Exo 2',sans-serif;color:var(--orange);letter-spacing:1.5px}
.brand-dot{width:12px;height:12px;border-radius:50%;background:var(--orange)}
.tagline{position:absolute;left:440px;top:152px;width:372px;height:23px;background:linear-gradient(180deg,#b0aca8,#8d8a87);border-radius:0 4px 4px 0;font:italic 400 9.5px/23px 'Arimo',sans-serif;color:#1c1c1c;padding-left:8px;white-space:nowrap}
.tagline b{font-weight:700}

/* navigation */
.main-nav{position:absolute;left:82px;top:190px;display:flex;gap:6px}
.nav-item{height:34px;border:2px solid #8e8c8a;border-radius:5px;background:linear-gradient(180deg,#2a2a2a,#0e0e0e);font:italic 800 13px/30px 'Exo 2',sans-serif;color:var(--white);text-align:center;letter-spacing:.3px;white-space:nowrap}
.nav-item.is-active{background:linear-gradient(180deg,var(--orange-light),var(--orange));color:var(--ink);border-color:#5a3a1e}
.w52{width:52px}.w80{width:80px}.w94{width:94px}.w64{width:64px}.w118{width:118px}.w134{width:134px}.w56{width:56px}.w98{width:98px}

.dropdown{position:absolute;left:147px;top:227px;width:148px;padding:3px 6px;background:#2b2b2b;border:1px solid #555;z-index:3}
.dropdown li{list-style:none;font:italic 800 9px/19px 'Exo 2',sans-serif;color:var(--white);border-bottom:1px solid #888;padding-left:14px;position:relative}
.dropdown li:last-child{border-bottom:0}
.dropdown li::before{content:"";position:absolute;left:2px;top:6px;border-left:6px solid var(--orange);border-top:4px solid transparent;border-bottom:4px solid transparent}

/* panels */
.panel{position:absolute;background:linear-gradient(180deg,var(--orange-mid),var(--orange));border-radius:8px 8px 0 0;padding:6px}
.panel-frame{height:100%;background:#080808;padding:6px}
.panel-body{height:100%;border:1px solid var(--panel-line);background:linear-gradient(180deg,#000 0,#111 50%,#333 100%)}
.main-panel{left:82px;top:232px;width:496px;height:417px}
.side-panel{left:586px;top:232px;width:234px;height:417px}
.wide-panel{left:82px;top:231px;width:738px;height:494px}

/* footer */
.call-bar{position:absolute;left:82px;width:738px;height:33px;background:linear-gradient(180deg,var(--orange-light),var(--orange) 70%);border-radius:6px;display:flex;align-items:flex-end;justify-content:flex-end;padding:0 2px 2px 0;gap:6px;color:var(--ink)}
.call-label{font:italic 800 12px/1 'Exo 2',sans-serif;padding-bottom:4px}
.call-number{font:italic 900 27px/1 'Exo 2',sans-serif}
.copyright{position:absolute;right:82px;font:400 10px/1 'Arimo',sans-serif;color:var(--orange);letter-spacing:.6px}

/* content type */
.kicker{position:absolute;left:120px;font:italic 300 30px/1 'Exo 2',sans-serif;color:var(--orange);white-space:nowrap}
.page-title{position:absolute;left:118px;font:italic 900 36px/1 'Exo 2',sans-serif;color:var(--white);white-space:nowrap}
.cabins-title{font-size:46px}
.copy{position:absolute;left:120px;font:400 12px/15px 'Arimo',sans-serif;color:var(--white);white-space:nowrap}
.copy p{margin-bottom:14px}
.cabins-copy{font-size:11.5px;line-height:15px}
.cabins-copy p{margin-bottom:14px}
.hl{color:var(--orange);font-weight:700}
.hl-soft{color:var(--orange)}

.figure{position:absolute;background:linear-gradient(160deg,#2a1a0e,#120c08);border:1px solid rgba(239,121,47,.35);border-radius:4px}
.fig-caption{position:absolute;font:400 9.5px/10px 'Arimo',sans-serif;color:var(--caption);white-space:nowrap}
.arrow{position:absolute}

/* sidebar */
.feature-btn{position:absolute;left:622px;width:160px;height:52px;border-radius:5px;background:linear-gradient(180deg,#f6b257,var(--orange) 55%,#e46d25);display:flex;align-items:center;justify-content:center;gap:8px;font:italic 800 15px/1 'Exo 2',sans-serif;color:var(--ink);box-shadow:0 2px 0 #7a3a12;white-space:nowrap}
.feature-text{position:absolute;left:586px;width:234px;text-align:center;font:400 11.5px/13.5px 'Arimo',sans-serif;color:var(--white)}
.feature-text b{color:var(--orange)}

/* cabins */
.gallery-photo{position:absolute;top:268px;height:75px}
.photo-loader{left:460px;width:106px;background:linear-gradient(135deg,#6d8fb8,#d3a21c 55%,#6a5b2c)}
.photo-cab{left:574px;width:100px;background:linear-gradient(135deg,#8a8a5a,#e8c81c 50%,#3d4a48)}
.photo-mower{left:682px;width:102px;background:linear-gradient(135deg,#c7c8c6,#b82424 55%,#3a3a3a)}
.blueprint{position:absolute;left:527px;top:363px;width:270px;height:130px;background:linear-gradient(180deg,#1a1a1a,#120b06);border:1px solid #3a3a3a}
.list-title{position:absolute;font:italic 600 13px/1 'Exo 2',sans-serif;color:var(--orange);letter-spacing:.4px;white-space:nowrap}
.spec-list{position:absolute;top:531px;list-style:none;font:400 12px/16.5px 'Arimo',sans-serif;color:var(--white);white-space:nowrap}
.spec-list li{padding-left:14px;position:relative}
.spec-list li::before{content:"";position:absolute;left:0;top:4px;border-left:8px solid var(--orange);border-top:4.5px solid transparent;border-bottom:4.5px solid transparent}
</style>
</head>
<body>
<div class="sheet">

  <!-- ===== Main page ===== -->
  <h2 class="sheet-label" style="top:31px">MAIN PAGE</h2>
  <section class="mock" style="top:63px;height:737px">
    <div class="banner">
      <div class="banner-photo photo-truck" role="img" aria-label="Yellow truck cab photo"><span>ROPS | FOPS</span></div>
      <div class="banner-photo photo-fabrication" role="img" aria-label="Steel fabrication frame photo"><span>FABRICATION</span></div>
      <div class="banner-photo photo-repairs" role="img" aria-label="White truck cab under repair photo"><span>REPAIRS</span></div>
    </div>
    <div class="brand-bar"><div class="brand-plate"><span class="brand-dot"></span><span class="brand-name">TARVEL FABRICATION</span></div></div>
    <p class="tagline">It's the <b>choice you make</b>, not the chance you take that determines your safety!</p>
    <nav class="main-nav">
      <span class="nav-item w52">HOME</span><span class="nav-item w80">ABOUT US</span><span class="nav-item w94">ROPS | FOPS</span><span class="nav-item w64">CABINS</span><span class="nav-item w118">CRANE REPAIRS</span><span class="nav-item w134">OTHER PRODUCTS</span><span class="nav-item w56">LINKS</span><span class="nav-item w98">CONTACT US</span>
    </nav>

    <div class="panel main-panel"><div class="panel-frame"><div class="panel-body"></div></div></div>
    <div class="panel side-panel"><div class="panel-frame"><div class="panel-body"></div></div></div>

    <p class="kicker" style="top:270px">Welcome to</p>
    <h1 class="page-title" style="top:303px">Tarvel Fabrication</h1>
    <div class="copy" style="top:357px">
      <p><span class="hl">Tarvel Fabrication leads the world</span><br>ur adipiscing elit. Cras egestas, turpi ac<br>elementum porta, justo mauris vu lputate<br>enim, nec volutpat nulla nunc non velit.</p>
      <p><span class="hl">Our ROPS are,</span> volutpat at varius<br>vul putate, sodales sit amet ante.<br>Integer tempor lectus nec nibh solli con<br>gue vivamus fermentum ege.</p>
      <p><span class="hl">Quality is</span> turpis ac elementum porta, justo<br>mauris vulputate enim, at usce tellus<br>nec volutpat usce tellus dui, vol utp var<br>iusnulla nunc non velit.</p>
      <p>Vul putate, sodales sit amet ante.<br>Integer tempor lectus nec nibh</p>
    </div>
    <div class="figure" style="left:382px;top:355px;width:140px;height:85px" role="img" aria-label="Orange line drawing of a ROPS cabin"></div>
    <svg class="arrow" style="left:447px;top:449px" width="12" height="34" viewBox="0 0 12 34"><path d="M6 0 L12 10 H8 V34 H4 V10 H0 Z" fill="#fff"/></svg>
    <p class="fig-caption" style="left:466px;top:473px">ROPS built<br>with quality</p>
    <div class="figure" style="left:387px;top:499px;width:118px;height:108px" role="img" aria-label="Orange line drawing of a ROPS frame"></div>
    <svg class="arrow" style="left:387px;top:540px" width="34" height="12" viewBox="0 0 34 12"><path d="M34 6 L24 0 V4 H0 V8 H24 V12 Z" fill="#fff"/></svg>
    <p class="fig-caption" style="left:379px;top:559px">ROPS built<br>safe</p>

    <div class="feature-btn" style="top:270px"><svg width="26" height="22" viewBox="0 0 26 22"><rect x="1" y="1" width="24" height="20" rx="3" fill="#fff"/><rect x="5" y="5" width="8" height="8" fill="#161616"/><path d="M15 6h7M15 10h7M5 16h17" stroke="#161616" stroke-width="2"/></svg>ROPS | FOPS</div>
    <p class="feature-text" style="top:328px"><b>TVF ROPS &amp; FOPS are</b><br>ur adipiscing elit. Cras, turpi<br>ac elementum porta.</p>
    <div class="feature-btn" style="top:392px"><svg width="30" height="22" viewBox="0 0 30 22"><rect x="1" y="3" width="26" height="17" rx="2" fill="#fff" stroke="#161616" stroke-width="1.5"/><path d="M1 4 L14 13 L27 4" fill="none" stroke="#161616" stroke-width="2"/></svg>CONTACT US</div>
    <p class="feature-text" style="top:450px"><b>You can reach us by</b><br>ur adipiscing elit. Cras, turpi<br>ac elementum porta.</p>
    <div class="feature-btn" style="top:515px"><svg width="24" height="24" viewBox="0 0 24 24"><rect x="2" y="1" width="20" height="22" rx="2" fill="#fff" stroke="#161616" stroke-width="1.5"/><path d="M6 7h12M6 11h12M6 15h12M6 19h8" stroke="#161616" stroke-width="2"/></svg>NEWSLETTER</div>
    <p class="feature-text" style="top:573px"><b>Sign up for our News</b><br>ur adipiscing elit. Cras, turpi<br>ac elementum porta.</p>

    <div class="call-bar" style="top:657px"><span class="call-label">CALL US ANYTIME</span><span class="call-number">07 4819 6307</span></div>
    <p class="copyright" style="top:699px">© 2009 Tarvel Fabrication Inc.</p>
  </section>

  <!-- ===== Main page + dropdown ===== -->
  <h2 class="sheet-label" style="top:856px">MAIN PAGE + DROPDOWN</h2>
  <section class="mock" style="top:888px;height:737px">
    <div class="banner">
      <div class="banner-photo photo-truck" role="img" aria-label="Yellow truck cab photo"><span>ROPS | FOPS</span></div>
      <div class="banner-photo photo-fabrication" role="img" aria-label="Steel fabrication frame photo"><span>FABRICATION</span></div>
      <div class="banner-photo photo-repairs" role="img" aria-label="White truck cab under repair photo"><span>REPAIRS</span></div>
    </div>
    <div class="brand-bar"><div class="brand-plate"><span class="brand-dot"></span><span class="brand-name">TARVEL FABRICATION</span></div></div>
    <p class="tagline">It's the <b>choice you make</b>, not the chance you take that determines your safety!</p>
    <nav class="main-nav">
      <span class="nav-item w52">HOME</span><span class="nav-item w80 is-active">ABOUT US</span><span class="nav-item w94">ROPS | FOPS</span><span class="nav-item w64">CABINS</span><span class="nav-item w118">CRANE REPAIRS</span><span class="nav-item w134">OTHER PRODUCTS</span><span class="nav-item w56">LINKS</span><span class="nav-item w98">CONTACT US</span>
    </nav>
    <ul class="dropdown">
      <li>MISSION AND VALUES</li><li>FACILITIES</li><li>TERMS AND CONDITIONS</li><li>JOBS</li>
    </ul>

    <div class="panel main-panel"><div class="panel-frame"><div class="panel-body"></div></div></div>
    <div class="panel side-panel"><div class="panel-frame"><div class="panel-body"></div></div></div>

    <p class="kicker" style="top:270px">Welcome to</p>
    <h1 class="page-title" style="top:303px">Tarvel Fabrication</h1>
    <div class="copy" style="top:357px">
      <p><span class="hl">Tarvel Fabrication leads the world</span><br>ur adipiscing elit. Cras egestas, turpi ac<br>elementum porta, justo mauris vu lputate<br>enim, nec volutpat nulla nunc non velit.</p>
      <p><span class="hl">Our ROPS are,</span> volutpat at varius<br>vul putate, sodales sit amet ante.<br>Integer tempor lectus nec nibh solli con<br>gue vivamus fermentum ege.</p>
      <p><span class="hl">Quality is</span> turpis ac elementum porta, justo<br>mauris vulputate enim, at usce tellus<br>nec volutpat usce tellus dui, vol utp var<br>iusnulla nunc non velit.</p>
      <p>Vul putate, sodales sit amet ante.<br>Integer tempor lectus nec nibh</p>
    </div>
    <div class="figure" style="left:382px;top:355px;width:140px;height:85px" role="img" aria-label="Orange line drawing of a ROPS cabin"></div>
    <svg class="arrow" style="left:447px;top:449px" width="12" height="34" viewBox="0 0 12 34"><path d="M6 0 L12 10 H8 V34 H4 V10 H0 Z" fill="#fff"/></svg>
    <p class="fig-caption" style="left:466px;top:473px">ROPS built<br>with quality</p>
    <div class="figure" style="left:387px;top:499px;width:118px;height:108px" role="img" aria-label="Orange line drawing of a ROPS frame"></div>
    <svg class="arrow" style="left:387px;top:540px" width="34" height="12" viewBox="0 0 34 12"><path d="M34 6 L24 0 V4 H0 V8 H24 V12 Z" fill="#fff"/></svg>
    <p class="fig-caption" style="left:379px;top:559px">ROPS built<br>safe</p>

    <div class="feature-btn" style="top:270px"><svg width="26" height="22" viewBox="0 0 26 22"><rect x="1" y="1" width="24" height="20" rx="3" fill="#fff"/><rect x="5" y="5" width="8" height="8" fill="#161616"/><path d="M15 6h7M15 10h7M5 16h17" stroke="#161616" stroke-width="2"/></svg>ROPS | FOPS</div>
    <p class="feature-text" style="top:328px"><b>TVF ROPS &amp; FOPS are</b><br>ur adipiscing elit. Cras, turpi<br>ac elementum porta.</p>
    <div class="feature-btn" style="top:392px"><svg width="30" height="22" viewBox="0 0 30 22"><rect x="1" y="3" width="26" height="17" rx="2" fill="#fff" stroke="#161616" stroke-width="1.5"/><path d="M1 4 L14 13 L27 4" fill="none" stroke="#161616" stroke-width="2"/></svg>CONTACT US</div>
    <p class="feature-text" style="top:450px"><b>You can reach us by</b><br>ur adipiscing elit. Cras, turpi<br>ac elementum porta.</p>
    <div class="feature-btn" style="top:515px"><svg width="24" height="24" viewBox="0 0 24 24"><rect x="2" y="1" width="20" height="22" rx="2" fill="#fff" stroke="#161616" stroke-width="1.5"/><path d="M6 7h12M6 11h12M6 15h12M6 19h8" stroke="#161616" stroke-width="2"/></svg>NEWSLETTER</div>
    <p class="feature-text" style="top:573px"><b>Sign up for our News</b><br>ur adipiscing elit. Cras, turpi<br>ac elementum porta.</p>

    <div class="call-bar" style="top:657px"><span class="call-label">CALL US ANYTIME</span><span class="call-number">07 4819 6307</span></div>
    <p class="copyright" style="top:699px">© 2009 Tarvel Fabrication Inc.</p>
  </section>

  <!-- ===== Content page: Cabins ===== -->
  <h2 class="sheet-label" style="top:1680px">CONTENT PAGE (CABINS)</h2>
  <section class="mock" style="top:1712px;height:800px">
    <div class="banner">
      <div class="banner-photo photo-truck" role="img" aria-label="Yellow truck cab photo"><span>ROPS | FOPS</span></div>
      <div class="banner-photo photo-fabrication" role="img" aria-label="Steel fabrication frame photo"><span>FABRICATION</span></div>
      <div class="banner-photo photo-repairs" role="img" aria-label="White truck cab under repair photo"><span>REPAIRS</span></div>
    </div>
    <div class="brand-bar"><div class="brand-plate"><span class="brand-dot"></span><span class="brand-name">TARVEL FABRICATION</span></div></div>
    <p class="tagline">It's the <b>choice you make</b>, not the chance you take that determines your safety!</p>
    <nav class="main-nav">
      <span class="nav-item w52">HOME</span><span class="nav-item w80">ABOUT US</span><span class="nav-item w94">ROPS | FOPS</span><span class="nav-item w64">CABINS</span><span class="nav-item w118">CRANE REPAIRS</span><span class="nav-item w134">OTHER PRODUCTS</span><span class="nav-item w56">LINKS</span><span class="nav-item w98">CONTACT US</span>
    </nav>

    <div class="panel wide-panel"><div class="panel-frame"><div class="panel-body"></div></div></div>

    <p class="kicker" style="top:272px">TVF specifications for</p>
    <h1 class="page-title cabins-title" style="top:302px">Cabins</h1>
    <div class="gallery-photo photo-loader" role="img" aria-label="Yellow loader cabin photo"></div>
    <div class="gallery-photo photo-cab" role="img" aria-label="Yellow fabricated cabin photo"></div>
    <div class="gallery-photo photo-mower" role="img" aria-label="Red ride-on mower with cabin photo"></div>

    <div class="copy cabins-copy" style="top:358px">
      <p><span class="hl-soft">Tarvel Fabrication are market leaders</span> in the design, fabrication and<br>installation of ROPS and non ROPS cabins to suit earthmoving and<br>mining equipment.</p>
      <p>When designing cabins, there are many <span class="hl-soft">key inputs</span> that must be<br>taken into account to ensure our cabins perform to our customers<br>expectations such as, visibility, aesthetics, access and functionality.<br>It is also important for a cabin to be similar in appearance to the<br>genuine article for machine resale purposes.</p>
    </div>

    <div class="blueprint" role="img" aria-label="Orange technical drawing of a cabin on a grid"></div>
    <p class="fig-caption" style="left:526px;top:413px">Mounting<br>Brackets</p>
    <svg class="arrow" style="left:737px;top:380px" width="32" height="12" viewBox="0 0 32 12"><path d="M0 6 L10 0 V4 H32 V8 H10 V12 Z" fill="#fff"/></svg>
    <p class="fig-caption" style="left:738px;top:398px">3mm<br>Steel Panels</p>

    <h3 class="list-title" style="left:117px;top:510px">CABIN STANDARD INCLUSIONS</h3>
    <h3 class="list-title" style="left:347px;top:510px">ADDITIONAL OPTIONS</h3>
    <ul class="spec-list" style="left:120px">
      <li>Front Windscreen Wiper and Washer</li><li>Interior Trim (roof only)</li><li>3 mm steel panels</li><li>Laminated glass</li><li>2- pack paint</li><li>Door seals, Latches &amp; Locks</li><li>Grab Handles</li><li>Mounting brackets</li><li>Roof guttering</li><li>Interior Lighting</li>
    </ul>
    <ul class="spec-list" style="left:352px">
      <li>R.O.P.S. Roll Over Protective Structure</li><li>F.O.P.S. Falling Objects Protective Structure</li><li>Full Interior Trim</li><li>Rear and Side vision mirrors</li><li>Floor covering</li><li>Additional wiper / washers required</li><li>Hidden interior wiring</li><li>Seat belt assembly</li><li>Suspension seats</li><li>Decals</li>
    </ul>
    <ul class="spec-list" style="left:612px">
      <li>Pressurized system</li><li>Air conditioning</li><li>Tinted Windows</li><li>Opening / sliding Windows</li><li>Roof mounted warning light/s</li>
    </ul>

    <div class="call-bar" style="top:733px"><span class="call-label">CALL US ANYTIME</span><span class="call-number">07 4819 6307</span></div>
    <p class="copyright" style="top:775px">© 2009 Tarvel Fabrication Inc.</p>
  </section>

</div>
</body>
</html>
```